New Company Business Card Design

I have a new company logo and I want a new business card design. I dont know if the logo file i attached is in the correct format or quality. We are a New York City Specialty construction Firm specializing in high risk out of the box projects. I want a simple and classy business card that people will his card is as crisp as the work his company does.

Target Market(s)

Clients in the heavy construction industry in New York City

Industry/Entity Type

Construction Company

Contact Information for Business Card

Simple Classy - DIFFERENT

Font styles to use
Other font styles liked:
• Mach the logo font in some way

Colors

Designer to choose colors to be used in the design.

Requirements
Must have
• Uniqueness
Nice to have
• Nothing particular - Just different and classy - Timeless
Should not have
• Goofy Shit or Gimmicky shit

```html
<!DOCTYPE html>
<html lang="en">
<head>
<meta charset="utf-8">
<title>Kestrel Builders – Business Card</title>
<link rel="stylesheet" href="https://fonts.googleapis.com/css2?family=Roboto:wght@400;700&display=swap">
<style>
  :root {
    --page-bg: #d8d5d1;
    --card-bg: #e8ebee;
    --card-edge: #cfd4d9;
    --navy: #14285a;
    --ink: #2b2f36;
    --icon: #1d2a4a;
    --crane-light: #c7ccd2;
    --crane-dark: #3a3d42;
  }
  * { margin: 0; padding: 0; box-sizing: border-box; }
  html, body {
    width: 1200px;
    height: 969px;
    overflow: hidden;
    background: var(--page-bg);
    font-family: "Roboto", Arial, sans-serif;
  }
  .card {
    position: absolute;
    left: 100px;
    top: 200px;
    width: 1000px;
    height: 568px;
    background: var(--card-bg);
    border: 1px solid var(--card-edge);
    box-shadow: 0 10px 30px rgba(0,0,0,0.15);
    overflow: hidden;
  }
  .company-name {
    position: absolute;
    left: 57px;
    top: 92px;
    display: flex;
    align-items: center;
    gap: 14px;
    color: var(--navy);
    font-weight: 700;
    font-size: 40px;
    letter-spacing: 1px;
    line-height: 1.1;
  }
  .company-name .mark {
    width: 30px;
    height: 30px;
    background: var(--navy);
  }
  .address {
    position: absolute;
    left: 57px;
    top: 290px;
    color: var(--ink);
    font-size: 24px;
    line-height: 32px;
  }
  .contacts {
    position: absolute;
    left: 57px;
    top: 366px;
    list-style: none;
    color: var(--ink);
    font-size: 24px;
  }
  .contacts li {
    display: flex;
    align-items: center;
    height: 32.5px;
  }
  .contacts svg {
    width: 22px;
    height: 22px;
    margin-right: 16px;
    fill: var(--icon);
  }
  .person {
    position: absolute;
    right: 72px;
    top: 84px;
    text-align: right;
    z-index: 2;
  }
  .person .name {
    color: var(--navy);
    font-weight: 700;
    font-size: 34px;
    letter-spacing: 0.5px;
  }
  .person .role {
    color: var(--ink);
    font-size: 24px;
    margin-top: 2px;
  }
  .crane-illustration {
    position: absolute;
    left: 464px;
    top: 12px;
    width: 536px;
    height: 556px;
    background: linear-gradient(160deg, rgba(199,204,210,0) 20%, var(--crane-light) 55%, var(--crane-dark) 100%);
  }
</style>
</head>
<body>
  <div class="card">
    <div class="crane-illustration" role="img" aria-label="Silhouette illustration of a lattice-boom construction crane with a hanging load"></div>

    <div class="company-name">
      <span class="mark"></span>
      <span>KESTREL<br>BUILDERS, INC.</span>
    </div>

    <div class="person">
      <div class="name">DANIEL REYES</div>
      <div class="role">CEO/FOUNDER</div>
    </div>

    <div class="address">
      412 Harbor Street<br>
      Brooklyn, New York 11201
    </div>

    <ul class="contacts">
      <li>
        <svg viewBox="0 0 24 24" aria-hidden="true"><path d="M6.6 10.8a15.1 15.1 0 0 0 6.6 6.6l2.2-2.2c.3-.3.7-.4 1-.2 1.1.4 2.3.6 3.6.6.6 0 1 .4 1 1V20c0 .6-.4 1-1 1A17 17 0 0 1 3 4c0-.6.4-1 1-1h3.5c.6 0 1 .4 1 1 0 1.3.2 2.5.6 3.6.1.3 0 .7-.2 1z"/></svg>
        718 555 0142
      </li>
      <li>
        <svg viewBox="0 0 24 24" aria-hidden="true"><path d="M7 1h10a2 2 0 0 1 2 2v18a2 2 0 0 1-2 2H7a2 2 0 0 1-2-2V3a2 2 0 0 1 2-2zm0 3v14h10V4zm5 15.5a1.2 1.2 0 1 0 0 2.4 1.2 1.2 0 0 0 0-2.4z"/></svg>
        917 555 0386
      </li>
      <li>
        <svg viewBox="0 0 24 24" aria-hidden="true"><path d="M6 2h12v5H6zM4 8h16a2 2 0 0 1 2 2v7h-4v5H6v-5H2v-7a2 2 0 0 1 2-2zm4 7v5h8v-5z"/></svg>
        718 555 0197
      </li>
      <li>
        <svg viewBox="0 0 24 24" aria-hidden="true"><path d="M2 5h20v14H2zm2 2v.5l8 5 8-5V7zm0 2.8V17h16V9.8l-8 5z"/></svg>
        office@kestrelbuild.com
      </li>
      <li>
        <svg viewBox="0 0 24 24" aria-hidden="true"><path d="M12 2a10 10 0 1 0 0 20 10 10 0 0 0 0-20zm6.9 6h-3a15 15 0 0 0-1.3-3.9A8 8 0 0 1 18.9 8zM12 4c.8 1.2 1.5 2.5 1.9 4h-3.8c.4-1.5 1.1-2.8 1.9-4zM4.3 14a8 8 0 0 1 0-4h3.4a16 16 0 0 0 0 4zm.8 2h3a15 15 0 0 0 1.3 3.9A8 8 0 0 1 5.1 16zm3-8h-3a8 8 0 0 1 4.3-3.9A15 15 0 0 0 8.1 8zM12 20c-.8-1.2-1.5-2.5-1.9-4h3.8c-.4 1.5-1.1 2.8-1.9 4zm2.3-6H9.7a14 14 0 0 1 0-4h4.6a14 14 0 0 1 0 4zm.3 5.9a15 15 0 0 0 1.3-3.9h3a8 8 0 0 1-4.3 3.9zm1.7-5.9a16 16 0 0 0 0-4h3.4a8 8 0 0 1 0 4z"/></svg>
        www.kestrelbuild.com
      </li>
    </ul>
  </div>
</body>
</html>
```